Martial art rank diploma

Need a diploma for a martial arts belt rank . The art is Japanese in origin , traditional is good , stylish , eye catching .
Dragons are good , no cartoon figures . Tacky is not good . Something proud to display
No martial art poses
Must have place for date , head instructor signature

And must say (a blank for students name )
"Having confirmed with all standards and requirements set forth by Brantwell Martial Arts and Fitness , is hereby promoted to the rank of " ( a blank for the rank)
Updates

Reason: nice designs, need to see more to compare

Industry/Entity Type

Martial Art

Requirements
Must have
• Logo attached and name of the school
Nice to have
• Dragon , that does not look like a centipede .

maybe best to have a dragon in the background as a water mark type of thing.
Should not have
• Tacky look or cartoon figures, or any martial art poses

```html
<!DOCTYPE html>
<html lang="en">
<head>
<meta charset="utf-8">
<title>Certificate of A Rank – Brantwell Martial Arts and Fitness</title>
<link rel="stylesheet" href="https://fonts.googleapis.com/css2?family=UnifrakturMaguntia&display=swap">
<style>
  :root {
    --frame-dark: #5e3a1c;
    --frame-light: #9a6b3d;
    --parchment-light: #f3dca6;
    --parchment-mid: #e9c98b;
    --parchment-edge: #d3a867;
    --ink: #1c1a17;
    --ink-line: #2a2622;
    --title-red: #6e1518;
    --title-edge: #2b0a0b;
    --dragon-tone: rgba(120, 112, 98, 0.38);
    --seal-red: #7a0f14;
    --seal-dark: #3f0507;
    --blackletter: "UnifrakturMaguntia", serif;
  }

  html, body {
    margin: 0;
    padding: 0;
    width: 1200px;
    height: 848px;
    overflow: hidden;
  }

  .canvas {
    position: relative;
    width: 1200px;
    height: 848px;
    background: linear-gradient(180deg, var(--frame-light), var(--frame-dark));
    font-family: var(--blackletter);
    color: var(--ink);
  }

  .parchment {
    position: absolute;
    left: 22px;
    top: 14px;
    width: 1156px;
    height: 820px;
    background:
      radial-gradient(ellipse at 55% 45%, var(--parchment-light) 0%, var(--parchment-mid) 60%, var(--parchment-edge) 100%);
    box-shadow: 0 0 14px rgba(0, 0, 0, 0.55), inset 0 0 40px rgba(140, 90, 40, 0.35);
  }

  .dragon-watermark {
    position: absolute;
    left: 70px;
    top: 95px;
    width: 1080px;
    height: 620px;
    border-radius: 45% 40% 45% 40%;
    background: radial-gradient(ellipse at 45% 50%, var(--dragon-tone) 0%, rgba(120, 112, 98, 0.18) 55%, rgba(120, 112, 98, 0) 75%);
  }

  .title {
    position: absolute;
    left: 0;
    top: 22px;
    width: 1170px;
    margin: 0;
    text-align: center;
    font-size: 84px;
    font-weight: 400;
    color: var(--title-red);
    text-shadow: 2px 2px 0 var(--title-edge), -1px -1px 0 #b98a7a, 3px 4px 6px rgba(0, 0, 0, 0.45);
    line-height: 1;
  }

  .line-text {
    position: absolute;
    margin: 0;
    white-space: nowrap;
    line-height: 1;
  }

  .certify { left: 100px; top: 212px; font-size: 54px; text-shadow: 1px 1px 2px rgba(0,0,0,0.4); }
  .date-row { left: 110px; top: 325px; font-size: 36px; }
  .date-row .day { position: absolute; left: 297px; }
  .date-row .year { position: absolute; left: 594px; }
  .statement { left: 64px; top: 402px; font-size: 37px; line-height: 60px; }
  .rank-label { left: 86px; top: 522px; font-size: 60px; text-shadow: 1px 1px 2px rgba(0,0,0,0.4); }
  .signature-role { left: 780px; top: 760px; font-size: 42px; }

  .fill-line {
    position: absolute;
    height: 0;
    border-top: 2px solid var(--ink-line);
  }
  .fill-line.student { left: 608px; top: 262px; width: 410px; }
  .fill-line.day-no { left: 245px; top: 355px; width: 148px; }
  .fill-line.month { left: 525px; top: 355px; width: 148px; }
  .fill-line.year-no { left: 928px; top: 355px; width: 180px; }
  .fill-line.rank { left: 495px; top: 580px; width: 608px; }
  .fill-line.signature { left: 775px; top: 737px; width: 307px; }

  .wax-seal {
    position: absolute;
    left: 468px;
    top: 630px;
    width: 190px;
    height: 190px;
    border-radius: 50%;
    background: radial-gradient(circle at 42% 38%, #a3262b 0%, var(--seal-red) 45%, var(--seal-dark) 100%);
    box-shadow: 2px 4px 8px rgba(0, 0, 0, 0.5);
  }

  .school-mark {
    position: absolute;
    left: 88px;
    top: 712px;
    display: flex;
    align-items: center;
    gap: 10px;
  }
  .school-mark .dot {
    width: 40px;
    height: 40px;
    border-radius: 50%;
    border: 3px solid var(--title-red);
    box-sizing: border-box;
  }
  .school-mark .school-name {
    font-family: var(--blackletter);
    font-size: 25px;
    line-height: 1.05;
    color: var(--title-red);
  }
</style>
</head>
<body>
  <main class="canvas">
    <section class="parchment">
      <div class="dragon-watermark" role="img" aria-label="Faint coiled Asian dragon watermark behind the certificate text"></div>

      <h1 class="title">Certificate of A Rank</h1>

      <p class="line-text certify">This is to certify that</p>
      <div class="fill-line student"></div>

      <p class="line-text date-row">On this<span class="day">day of</span><span class="year">in the year of</span></p>
      <div class="fill-line day-no"></div>
      <div class="fill-line month"></div>
      <div class="fill-line year-no"></div>

      <p class="line-text statement">Having confirmed with all standards and requirements set forth<br>by Brantwell Martial Arts and Fitness is here by promoted to</p>

      <p class="line-text rank-label">The Rank Of</p>
      <div class="fill-line rank"></div>

      <div class="wax-seal" role="img" aria-label="Red wax seal"></div>

      <div class="school-mark">
        <span class="dot"></span>
        <span class="school-name">Brantwell<br>Martial Arts and Fitness</span>
      </div>

      <div class="fill-line signature"></div>
      <p class="line-text signature-role">Head Instructor</p>
    </section>
  </main>
</body>
</html>
```